R. Vantello needs an original business card for property investment professionals

The business card would be to present me as an investor in the real estate business. The market are developers of real estate projects, or other people who would like to sell and also to give us a name as a company. For style, colour and imagery I would like something artistic from Vantello (the artist) with a different touch.

Address, email, cel phone,
Updates

Hi¡ Update¡ I;d like it to stop providing Bright Ledger as a Design and focus in R.Vantello.

Target Market(s)

Real Estate Developer/Investor

Industry/Entity Type

Real Estate

Colors
33a6d7
886aae
e3daeb
cadf82
f78f20

```html
<!DOCTYPE html>
<html lang="en">
<head>
<meta charset="utf-8">
<title>R. Vantello – Realtor Business Card</title>
<link rel="stylesheet" href="https://fonts.googleapis.com/css2?family=Tinos&family=Comic+Neue:wght@700&family=Noto+Sans&display=swap">
<style>
  :root {
    --blue: #1e8fd6;
    --blue-deep: #2f5fae;
    --orange: #e9791c;
    --paper: #ffffff;
    --ink: #222222;
    --ochre: #c99a3e;
    --olive: #7d8a5c;
  }
  * { box-sizing: border-box; margin: 0; padding: 0; }
  html, body { width: 1200px; height: 1009px; overflow: hidden; background: var(--paper); }
  .canvas { position: relative; width: 1200px; height: 1009px; }

  /* Front side */
  .card-front { position: absolute; left: 0; top: 0; width: 590px; height: 940px; overflow: hidden; }
  .front-backdrop {
    position: absolute; left: 0; top: 0; width: 590px; height: 345px;
    background: linear-gradient(180deg, #f7f3ea 0%, #efe9dc 100%);
  }
  .brand-name {
    position: absolute; left: 0; top: 130px; width: 590px; text-align: center;
    font-family: "Tinos", serif; font-size: 72px; color: var(--orange);
  }
  .title-panel {
    position: absolute; left: 0; top: 345px; width: 310px; height: 595px; background: var(--blue);
  }
  .title-rule {
    position: absolute; left: 34px; top: 410px; width: 224px; height: 3px; background: var(--paper);
  }
  .title-label {
    position: absolute; left: 34px; top: 422px; width: 224px; text-align: center;
    font-family: "Tinos", serif; font-size: 30px; color: var(--paper);
  }
  .property-photo {
    position: absolute; left: 310px; top: 345px; width: 272px; height: 595px;
    background: linear-gradient(180deg, #6f8a5f 0%, #3f73c6 35%, #2e63c0 60%, #d9d6cf 80%, #c8c4bb 100%);
  }
  .artwork {
    position: absolute; left: 10px; top: 494px; width: 412px; height: 390px; border-radius: 50%;
    border: 9px solid var(--paper);
    background: radial-gradient(circle at 45% 45%, var(--ochre) 0%, var(--olive) 55%, #9a4e2a 100%);
  }

  /* Back side */
  .card-back { position: absolute; left: 620px; top: 0; width: 580px; height: 940px; }
  .card-back svg { display: block; }
  .back-title {
    font-family: "Comic Neue", sans-serif; font-weight: 700; font-size: 190px; fill: var(--orange);
  }
  .contact-glyph { fill: none; stroke: var(--paper); stroke-width: 4; stroke-linecap: round; stroke-linejoin: round; }
  .contact-text { font-family: "Comic Neue", sans-serif; font-weight: 700; font-size: 22px; fill: var(--blue-deep); }

  .side-label {
    position: absolute; top: 962px; width: 200px; text-align: center;
    font-family: "Noto Sans", sans-serif; font-size: 36px; color: var(--ink);
  }
  .side-label.front { left: 156px; }
  .side-label.back { left: 738px; }
</style>
</head>
<body>
<main class="canvas">
  <section class="card-front">
    <div class="front-backdrop" role="img" aria-label="Faded painting of village houses behind the brand name"></div>
    <div class="brand-name">R. Vantello</div>
    <div class="title-panel"></div>
    <div class="title-rule"></div>
    <div class="title-label">Realtor</div>
    <div class="property-photo" role="img" aria-label="Photograph of a blue swimming pool with palm trees and loungers"></div>
    <div class="artwork" role="img" aria-label="Cubist painting of factory buildings and palm trees in ochre and green"></div>
  </section>

  <section class="card-back">
    <svg width="580" height="940" viewBox="0 0 580 940">
      <rect width="580" height="940" fill="var(--paper)"/>
      <path d="M300 0 L580 0 L580 330 Q560 90 300 0 Z" fill="var(--orange)"/>
      <path d="M10 940 Q440 860 470 420 Q490 220 580 190 L580 940 Z" fill="var(--blue)"/>
      <text class="back-title" transform="translate(565 790) rotate(-90)">Realtor</text>

      <g class="contact-email">
        <circle cx="269" cy="262" r="30" fill="var(--orange)"/>
        <rect class="contact-glyph" x="254" y="252" width="30" height="21" rx="2"/>
        <path class="contact-glyph" d="M254 253 L269 264 L284 253"/>
        <text class="contact-text" x="310" y="270">rv@vantello.co</text>
      </g>
      <g class="contact-phone">
        <circle cx="216" cy="368" r="30" fill="var(--orange)"/>
        <path class="contact-glyph" d="M205 356 q-4 14 12 26 q10 6 14 2 l3 -5 l-7 -6 l-4 3 q-7 -4 -10 -11 l4 -3 l-4 -8 Z"/>
        <text class="contact-text" x="258" y="376">+1 555 014 2290</text>
      </g>
      <g class="contact-social">
        <circle cx="168" cy="482" r="14" fill="var(--blue-deep)"/>
        <text class="contact-text" x="192" y="490">Linkfold /rvantello</text>
      </g>
      <g class="contact-social">
        <circle cx="120" cy="610" r="14" fill="var(--blue)"/>
        <text class="contact-text" x="144" y="618">Chirpline @rvantello</text>
      </g>
      <g class="contact-web">
        <rect x="60" y="714" width="26" height="26" fill="var(--blue-deep)"/>
        <text class="contact-text" x="98" y="735">www.vantello.co</text>
      </g>
    </svg>
  </section>

  <div class="side-label front">Front</div>
  <div class="side-label back">Back</div>
</main>
</body>
</html>
```